Vexor Mind Social Media Advertisement

We need a social media advertisement made up for our Asset Insight. Our initial campaign will be on Reddit, so it needs to be compliant with reddit. Attached is a brief, we just need 1 single design initially that we can interchange the copy to see what converts better. Must be in a format that we can easily edit. Attached also are some examples of advertisements that are currently posted on Reddit for similar products. Coinsprig is the closest competitor. Please visit our website: https://www.vexormind.example to understand more about the business. You can also register as a free user to view the platform.

Target Market(s)

Self-directed Australian investors — particularly Self managed super fund trustees and property investors — who actively manage their own wealth and want AI-powered insights to make smarter financial decisions.

Industry/Entity Type

Financial technology (FinTech) / Wealth management software.

Requirements
Must have
• Dark, sophisticated colour palette (navy and teal), no emoji or decorative icons, clean and modern typography, and imagery that conveys intelligence, data, and financial confidence — not generic stock market clichés.
Nice to have
• Subtle futuristic or tech aesthetic, data visualisation elements (charts, graphs, network nodes), a sense of calm authority rather than aggressive "get rich" energy, and designs that would work across both digital ads and print formats.
Should not have
• Bright or garish colours, cartoonish illustrations, generic stock market imagery (bulls, bears, ticker tape), cluttered layouts, anything that feels salesy or hype-driven, and no cryptocurrency or "get rich quick" visual cues.

```html
<!DOCTYPE html>
<html lang="en">
<head>
<meta charset="utf-8">
<title>Vexor Mind — Retirement Projection Ad</title>
<link rel="stylesheet" href="https://fonts.googleapis.com/css2?family=Fira+Sans:ital,wght@0,400;0,500;0,600;1,400&display=swap">
<style>
  :root {
    --navy-deep: #02122b;
    --navy-panel: #06224a;
    --white: #f4f7fb;
    --teal: #39e6d6;
    --teal-soft: #8ff3ea;
    --label: #dbe6f2;
    --rule: rgba(160, 190, 220, 0.35);
    --grid: rgba(110, 160, 210, 0.16);
  }
  * { margin: 0; padding: 0; box-sizing: border-box; }
  html, body { width: 1200px; height: 800px; overflow: hidden; background: var(--navy-deep); }
  .ad {
    position: relative;
    width: 1200px;
    height: 800px;
    background: radial-gradient(ellipse at 50% 40%, #061a3a 0%, var(--navy-deep) 70%);
    font-family: "Fira Sans", Arial, sans-serif;
    overflow: hidden;
  }
  .chart { position: absolute; left: 0; top: 0; width: 1200px; height: 800px; }
  .headline {
    position: absolute;
    left: 53px;
    top: 252px;
    color: var(--white);
    font-size: 38px;
    font-weight: 500;
    line-height: 51px;
    letter-spacing: -0.2px;
  }
  .headline-rule {
    position: absolute;
    left: 52px;
    top: 366px;
    width: 534px;
    height: 1px;
    background: linear-gradient(90deg, var(--rule), rgba(160,190,220,0.15));
  }
  .brand-line {
    position: absolute;
    left: 53px;
    top: 384px;
    font-size: 17px;
    color: var(--teal);
  }
  .brand-name { font-weight: 600; font-style: normal; }
  .brand-tagline { font-style: italic; font-weight: 400; }
  .data-label {
    position: absolute;
    color: var(--label);
    font-size: 14px;
    font-weight: 400;
    white-space: nowrap;
  }
  .data-label strong { font-weight: 600; color: var(--white); }
  .data-label.target { color: var(--teal-soft); font-size: 16.5px; }
  .axis-label {
    position: absolute;
    top: 510px;
    color: var(--white);
    font-size: 15px;
    font-weight: 600;
    transform: translateX(-50%);
  }
</style>
</head>
<body>
<div class="ad">
  <svg class="chart" viewBox="0 0 1200 800" aria-hidden="true">
    <defs>
      <linearGradient id="panel-fill" x1="0" y1="0" x2="1" y2="0">
        <stop offset="0" stop-color="#06224a" stop-opacity="0"/>
        <stop offset="0.45" stop-color="#06224a" stop-opacity="0.7"/>
        <stop offset="1" stop-color="#07295a" stop-opacity="0.9"/>
      </linearGradient>
      <linearGradient id="area-fill" x1="0" y1="0" x2="0" y2="1">
        <stop offset="0" stop-color="#2fd6cf" stop-opacity="0.35"/>
        <stop offset="1" stop-color="#2fd6cf" stop-opacity="0"/>
      </linearGradient>
      <linearGradient id="line-stroke" x1="0" y1="0" x2="1" y2="0">
        <stop offset="0" stop-color="#39e6d6" stop-opacity="0.2"/>
        <stop offset="0.3" stop-color="#39e6d6"/>
        <stop offset="0.85" stop-color="#c8fff9"/>
        <stop offset="1" stop-color="#6ff0e4"/>
      </linearGradient>
      <radialGradient id="node-glow">
        <stop offset="0" stop-color="#9ffff5" stop-opacity="0.8"/>
        <stop offset="1" stop-color="#39e6d6" stop-opacity="0"/>
      </radialGradient>
      <filter id="blur"><feGaussianBlur stdDeviation="4"/></filter>
    </defs>

    <rect class="chart-panel" x="312" y="199" width="888" height="387" fill="url(#panel-fill)"/>

    <g class="grid" stroke="var(--grid)" stroke-width="1">
      <line x1="555" y1="420" x2="555" y2="512"/>
      <line x1="602" y1="400" x2="602" y2="512"/>
      <line x1="648" y1="380" x2="648" y2="512"/>
      <line x1="688" y1="360" x2="688" y2="512"/>
      <line x1="731" y1="330" x2="731" y2="512"/>
      <line x1="774" y1="300" x2="774" y2="512"/>
      <line x1="816" y1="225" x2="816" y2="512"/>
      <line x1="859" y1="225" x2="859" y2="512"/>
      <line x1="898" y1="225" x2="898" y2="512"/>
      <line x1="945" y1="225" x2="945" y2="512"/>
      <line x1="988" y1="225" x2="988" y2="512"/>
      <line x1="1074" y1="225" x2="1074" y2="512"/>
      <line x1="1117" y1="225" x2="1117" y2="512"/>
      <line x1="1160" y1="225" x2="1160" y2="512"/>
      <line x1="600" y1="327" x2="1200" y2="327" stroke-dasharray="3 4"/>
      <line x1="600" y1="355" x2="1200" y2="355"/>
      <line x1="560" y1="379" x2="1200" y2="379" stroke-dasharray="3 4"/>
      <line x1="560" y1="430" x2="1200" y2="430" stroke-dasharray="3 4"/>
      <line x1="816" y1="250" x2="1200" y2="250"/>
    </g>

    <line class="axis" x1="330" y1="501" x2="1200" y2="501" stroke="rgba(170,200,230,0.45)" stroke-width="1.2"/>
    <line class="marker-drop" x1="1031" y1="324" x2="1031" y2="501" stroke="rgba(150,220,230,0.45)" stroke-width="1"/>

    <path class="projection-area" d="M484 496 C600 490 700 476 780 450 C880 412 960 360 1031 324 C1045 327 1055 327 1062 327 C1100 315 1130 300 1160 289 L1160 501 L484 501 Z" fill="url(#area-fill)" opacity="0.6"/>
    <path class="projection-glow" d="M328 500 C400 499 440 498 484 496 C600 490 700 476 780 450 C880 412 960 360 1031 324 C1045 327 1055 327 1062 327 C1100 315 1130 300 1160 289" fill="none" stroke="#39e6d6" stroke-width="8" opacity="0.45" filter="url(#blur)"/>
    <path class="projection-line" d="M328 500 C400 499 440 498 484 496 C600 490 700 476 780 450 C880 412 960 360 1031 324 C1045 327 1055 327 1062 327 C1100 315 1130 300 1160 289" fill="none" stroke="url(#line-stroke)" stroke-width="3"/>

    <circle class="start-node" cx="484" cy="496" r="5" fill="var(--teal)"/>
    <circle class="target-glow" cx="1031" cy="324" r="34" fill="url(#node-glow)"/>
    <circle class="target-ring" cx="1031" cy="324" r="19" fill="none" stroke="rgba(180,255,250,0.5)" stroke-width="1.5"/>
    <circle class="target-node" cx="1031" cy="324" r="10" fill="#ffffff"/>

    <line class="target-rule" x1="795" y1="284" x2="955" y2="284" stroke="rgba(160,200,230,0.45)" stroke-width="1"/>
  </svg>

  <h1 class="headline">See exactly when you can retire.<br>Then build the path to get there.</h1>
  <div class="headline-rule"></div>
  <p class="brand-line"><span class="brand-name">Vexor Mind</span> — <span class="brand-tagline">Asset Insight for the Self-Directed Investor</span></p>

  <p class="data-label target" style="left:794px; top:261px;">Retirement Age: 62</p>
  <p class="data-label target" style="left:794px; top:287px;">Projected Savings: $1.2M</p>
  <p class="data-label" style="left:621px; top:365px;">Current Savings: <strong>$350K</strong></p>
  <p class="data-label" style="left:621px; top:390px;">Monthly Contributions: <strong>$1,500</strong></p>

  <span class="axis-label" style="left:480px;">Now</span>
  <span class="axis-label" style="left:1037px;">Future</span>
</div>
</body>
</html>
```